LORM Business Card Design Project

Company Name: LORM (Bright Harbor Computing Solutions) PGH.
Office Address: Office No 718, Saffron Crest Tower, Palmwood Garden Heights, Dubai, U.A.E
Company line of business:
1) Currently we have a POS solution for retail outlets like duty free shops, supermarkets, department stores etc... The solution is deployed in Coastline Travel Retail on 350 POS and in Sandgate Airport Retail on 100 POS. So our main line of business is the deployment of this solution in retail outlets locally or regionally. We have already deployed the solution in India and Australia.
2) Integration of other third party POS systems with an online credit authorization netwotk in the UAE. This will enable POS applications to connect directly to the acquiring banks without needing an EFT terminal like Paxtrel or Movarski. The credit card payment is completed at the POS.
3) Other solutions that are targeting retail outlets like mobile POS, queue busting solutions, stock taking solutions using hand held devices, transaction capture systems, etc...
4) Other IT services like support of call center solutions from Northwind Callworks and development of new solutions as per customer requirements.
We need a business card design for the company. We don't have any specific requirements and will eave up to the designers to come up with creative designs. At the moment we still don't have a letter head design and the only thing that we have is the company logo that we will upload shortly.
Updates
Dear All,
I just uploaded the logo source files. I am sorry for the delay.
Regards
Samir Odwani
I would like the business cards to have the following details:
Company Tel No
Company Fax No
Company Website Address
Employee Name
Employee Title
Employee Mobile Number
Employee Email Address

```html
<!DOCTYPE html>
<html lang="en">
<head>
<meta charset="utf-8">
<title>Bright Harbor Computing Solutions – Business Card</title>
<link rel="stylesheet" href="https://fonts.googleapis.com/css2?family=Open+Sans:wght@400;700&family=Roboto+Condensed:wght@700&display=swap">
<style>
  :root {
    --brand-blue: #27aae1;
    --soft-grey: #f2f2f2;
    --card-border: #8a8a8a;
    --ink: #111111;
    --white: #ffffff;
    --canvas: #ffffff;
  }
  html, body {
    margin: 0;
    padding: 0;
    width: 1200px;
    height: 893px;
    overflow: hidden;
    background: var(--canvas);
  }
  .canvas {
    position: relative;
    width: 1200px;
    height: 893px;
  }
  .card {
    position: absolute;
    width: 620px;
    height: 401px;
    box-sizing: border-box;
    overflow: hidden;
  }
  .card--front {
    left: 44px;
    top: 43px;
    background: var(--white);
    border: 1px solid var(--card-border);
  }
  .card--back {
    left: 553px;
    top: 480px;
    height: 400px;
    background: var(--brand-blue);
    display: flex;
    align-items: center;
    justify-content: center;
  }
  .card__shapes {
    position: absolute;
    left: -1px;
    top: -1px;
    width: 620px;
    height: 401px;
  }
  .shape--grey { fill: var(--soft-grey); }
  .shape--blue { fill: var(--brand-blue); }

  .company-name {
    font-family: "Roboto Condensed", "Arial Narrow", sans-serif;
    font-weight: 700;
    letter-spacing: -0.3px;
    margin: 0;
    white-space: nowrap;
  }
  .card--front .company-name {
    position: absolute;
    left: 22px;
    top: 24px;
    font-size: 31px;
    line-height: 40px;
    color: var(--brand-blue);
  }
  .card--back .company-name {
    font-size: 37px;
    line-height: 44px;
    color: var(--white);
    margin-top: -10px;
  }

  .contact {
    position: absolute;
    left: 368px;
    top: 190px;
    color: var(--white);
    font-family: "Open Sans", Arial, sans-serif;
  }
  .contact__name {
    margin: 0;
    font-size: 25px;
    font-weight: 700;
    line-height: 32px;
  }
  .contact__line {
    margin: 0;
    font-size: 18px;
    line-height: 25px;
  }

  .address {
    position: absolute;
    left: 22px;
    top: 318px;
    font-family: "Open Sans", Arial, sans-serif;
    font-size: 13px;
    line-height: 19px;
    color: var(--ink);
    font-style: normal;
    letter-spacing: -0.2px;
  }
  .address__label {
    font-weight: 700;
    display: block;
  }
</style>
</head>
<body>
<main class="canvas">
  <section class="card card--front" aria-label="Business card front">
    <svg class="card__shapes" viewBox="0 0 620 401" aria-hidden="true">
      <polygon class="shape--grey" points="0,171 620,401 0,401"/>
      <polygon class="shape--blue" points="620,2 228,255 620,401"/>
    </svg>
    <h1 class="company-name">Bright Harbor Computing Solutions</h1>
    <div class="contact">
      <p class="contact__name">Your Name</p>
      <p class="contact__line">name@harbormail.com</p>
      <p class="contact__line">021 55501 234</p>
    </div>
    <address class="address">
      <span class="address__label">Office Address:</span>
      Office No 718, Saffron Crest Tower,<br>
      Palmwood Garden Heights, Dubai, U.A.E
    </address>
  </section>

  <section class="card card--back" aria-label="Business card back">
    <h2 class="company-name">Bright Harbor Computing Solutions</h2>
  </section>
</main>
</body>
</html>
```